Orvath Commentary

Looking for a book and e book cover... (not ready to provide specs yet), but wanting to see creative designs.
This is a NEW commentary on the Book of Orvath. The essence of this book is as follows:
1) there are thousands of commentaries on the book of Orvath but all basically have the same interpretations - just personalized. This is clearly a very new interpretation.
2) Rather than a commentary that follows along using a "historical" approach, I have looked for the Messiah in the verses and thus come away with these new interpretations,
3) the book will / should be titled as follows:
Commentary of the Book of Orvath (top)
Creative image (center / field)
somewhere within image area - "Can you see my now..."
4) The "Can you see me now" statement is made by Kelmar with His image but not a traditional image of Him.
5) Because no one has looked for Him in Orvath this will be a play of contradiction - it might be an image of Him that one knows it is Kelmar but you still can not see Him,
6) I will attach a word file which captures some images from the website (belong to others) to give you some thought on what I like.. look forward to seeing (without restricting your creative process at all),
There is no rush on completing this at this time... this deadline can easily be extended to 2/15/23

```html
<!DOCTYPE html>
<html lang="en">
<head>
<meta charset="utf-8">
<title>Commentary of the Book of Orvath — Cover Wrap</title>
<link href="https://fonts.googleapis.com/css2?family=Archivo+Black&family=Arimo:wght@400;700&display=swap" rel="stylesheet">
<style>
  :root {
    --page-bg: #ecebe8;
    --sky-top: #2f78c0;
    --sky-mid: #7fb4e0;
    --sky-glow: #eef6fd;
    --sky-low: #4f86b8;
    --sky-deep: #0f3462;
    --cloud-light: #dbe9f6;
    --cloud-mid: #8fb6da;
    --ridge-dark: #1c4673;
    --title-navy: #0d4a8c;
    --ink-dark: #14233a;
    --white: #ffffff;
    --spine-rule: #c8525a;
  }
  * { margin: 0; padding: 0; box-sizing: border-box; }
  html, body { width: 1200px; height: 800px; overflow: hidden; }
  body {
    background: var(--page-bg);
    font-family: "Arimo", Arial, sans-serif;
    position: relative;
  }
  .cover-wrap {
    position: absolute;
    left: 95px; top: 40px;
    width: 1010px; height: 720px;
    display: flex;
    box-shadow: 0 6px 24px rgba(0,0,0,.18);
    overflow: hidden;
  }
  .panel { position: relative; height: 100%; overflow: hidden; }
  .back-cover { width: 480px; }
  .spine { width: 50px; }
  .front-cover { width: 480px; }

  .cover-art { position: absolute; inset: 0; }
  .back-cover .cover-art {
    background:
      radial-gradient(ellipse 60% 35% at 70% 12%, rgba(238,246,253,.85), transparent 70%),
      radial-gradient(ellipse 70% 20% at 40% 78%, rgba(219,233,246,.55), transparent 75%),
      linear-gradient(180deg, var(--sky-top) 0%, var(--sky-mid) 35%, #9cc6e8 55%, var(--sky-low) 78%, var(--sky-deep) 100%);
  }
  .spine .cover-art {
    background: linear-gradient(180deg, #6aa6d8 0%, #b9d7ef 35%, #8bb7dd 60%, #3d6fa5 85%, var(--sky-deep) 100%);
  }
  .front-cover .cover-art {
    background:
      radial-gradient(ellipse 55% 30% at 40% 42%, var(--sky-glow), transparent 75%),
      linear-gradient(180deg, #3f86c9 0%, #9fcaec 25%, #dcecf8 42%, #a8c8e4 58%, var(--sky-low) 76%, var(--sky-deep) 100%);
  }
  .cover-photo {
    position: absolute; left: 0; right: 0; top: 300px; bottom: 0;
    background:
      radial-gradient(ellipse 35% 28% at 62% 32%, rgba(255,255,255,.75), transparent 75%),
      radial-gradient(ellipse 45% 30% at 85% 20%, rgba(219,233,246,.8), transparent 75%),
      radial-gradient(ellipse 40% 25% at 20% 45%, rgba(143,182,218,.7), transparent 75%),
      radial-gradient(ellipse 55% 30% at 75% 95%, var(--ridge-dark), transparent 80%),
      linear-gradient(180deg, rgba(219,233,246,0) 0%, var(--cloud-light) 20%, var(--cloud-mid) 55%, var(--sky-low) 75%, var(--sky-deep) 100%);
  }
  .spine-rule { position: absolute; top: 0; bottom: 0; width: 1px; background: var(--spine-rule); }
  .spine-rule.left { left: 0; }
  .spine-rule.right { right: 0; }

  .front-title {
    position: absolute; left: 40px; top: 60px; width: 400px;
    font-family: "Archivo Black", "Arial Black", sans-serif;
    color: var(--title-navy);
    text-transform: uppercase;
    letter-spacing: -2px;
    line-height: .95;
    text-align: right;
  }
  .front-title .line { display: block; font-size: 44px; }
  .front-title .line-name { font-size: 66px; }
  .front-title .small { font-size: 44px; }
  .tagline {
    position: absolute; left: 40px; top: 250px; width: 400px;
    text-align: center;
    font-size: 17px; letter-spacing: 4px;
    color: var(--ink-dark);
    text-transform: uppercase;
  }

  .spine-title {
    position: absolute; left: 50%; top: 30px;
    transform-origin: left top;
    transform: translateX(10px) rotate(90deg);
    white-space: nowrap;
    font-weight: 700; font-size: 15px;
    color: var(--title-navy);
    text-transform: uppercase;
    letter-spacing: .5px;
  }

  .back-title {
    position: absolute; left: 0; right: 0; top: 48px;
    text-align: center;
    font-family: "Archivo Black", "Arial Black", sans-serif;
    color: var(--white);
    text-transform: uppercase;
    letter-spacing: -1px;
    line-height: .95;
  }
  .back-title .line { display: block; font-size: 22px; }
  .back-title .line-name { font-size: 34px; }
  .back-title .small { font-size: 22px; }

  .back-copy {
    position: absolute; left: 50px; top: 165px; width: 380px;
    color: var(--ink-dark);
    font-size: 11px; line-height: 1.32;
    text-align: justify;
  }
  .back-copy p + p { margin-top: 12px; }
  .back-copy-closing {
    position: absolute; left: 115px; top: 590px; width: 315px;
    color: var(--ink-dark);
    font-size: 11px; line-height: 1.32;
    text-align: justify;
  }
  .imprint-mark {
    position: absolute; left: 50px; top: 612px;
    width: 44px; height: 44px; background: var(--white);
  }
</style>
</head>
<body>
  <main class="cover-wrap">
    <section class="panel back-cover">
      <div class="cover-art" aria-hidden="true"></div>
      <h2 class="back-title">
        <span class="line">Commentary</span>
        <span class="line">Of the Book</span>
        <span class="line"><span class="small">Of </span><span class="line-name">Orvath</span></span>
      </h2>
      <div class="back-copy">
        <p>Lorem ipsum dolor sit amet, consectetur adipiscing elit, sed do eiusmod tempor incididunt ut labore et dolore magna aliqua. Ut enim ad minim veniam, quis nostrud exercitation ullamco laboris nisi ut aliquip ex ea commodo consequat. Duis aute irure dolor in reprehenderit in voluptate velit esse cillum dolore eu fugiat nulla pariatur. Excepteur sint occaecat cupidatat non proident, sunt in culpa qui officia deserunt mollit anim id est laborum.</p>
        <p>Lorem ipsum dolor sit amet, consectetur adipiscing elit, sed do eiusmod tempor incididunt ut labore et dolore magna aliqua. Ut enim ad minim veniam, quis nostrud exercitation ullamco laboris nisi ut aliquip ex ea commodo consequat. Duis aute irure dolor in reprehenderit in voluptate velit esse cillum dolore eu fugiat nulla pariatur. Excepteur sint occaecat cupidatat non proident, sunt in culpa qui officia deserunt mollit anim id est laborum.</p>
        <p>Lorem ipsum dolor sit amet, consectetur adipiscing elit, sed do eiusmod tempor incididunt ut labore et dolore magna aliqua. Ut enim ad minim veniam, quis nostrud exercitation ullamco laboris nisi ut aliquip ex ea commodo consequat. Duis aute irure dolor in reprehenderit in voluptate velit esse cillum dolore eu fugiat nulla pariatur. Excepteur sint occaecat cupidatat non proident, sunt in culpa qui officia deserunt mollit anim id est laborum.</p>
      </div>
      <div class="imprint-mark"></div>
      <p class="back-copy-closing">Lorem ipsum dolor sit amet, consectetur adipiscing elit, sed do eiusmod tempor incididunt ut labore et dolore magna aliqua. Ut enim ad minim veniam, quis nostrud exercitation ullamco laboris nisi ut aliquip ex ea commodo consequat. Duis aute irure dolor in reprehenderit in voluptate velit esse cillum dolore eu fugiat nulla pariatur. Excepteur sint occaecat cupidatat non proident, sunt in culpa qui officia deserunt mollit anim id est laborum.</p>
    </section>

    <section class="panel spine">
      <div class="cover-art" aria-hidden="true"></div>
      <span class="spine-rule left"></span>
      <span class="spine-rule right"></span>
      <h2 class="spine-title">Commentary of the Book of Orvath</h2>
    </section>

    <section class="panel front-cover">
      <div class="cover-art" aria-hidden="true"></div>
      <div class="cover-photo" role="img" aria-label="Photograph: bright clouds below a glowing sky, a silhouetted figure with outstretched arms standing on a dark mountain peak"></div>
      <h1 class="front-title">
        <span class="line">Commentary</span>
        <span class="line">Of the Book</span>
        <span class="line"><span class="small">Of </span><span class="line-name">Orvath</span></span>
      </h1>
      <p class="tagline">Can you see my now...</p>
    </section>
  </main>
</body>
</html>
```